Fall for Display rack for Fall Plant program to be displayed in Yard Vault

Signage for retail plant promotion for fall. Should picture a front porch with fall plants and have our logo on the bottom and the yard vault logo. Could feature fall items like pumkins, cinnamon, gords and more. Should have promotional tital Fresh for Fall! Should have the following selling components as well - Natural Front Door Decor / Enjoy Warm & Cozy Color/ Generate Fall Fresh Air. All should look festive, fresh and have a white wood background. Sign will measure 3 to 4 foot tall by 22.2inches
Target Market(s)
Mass Market Retail - Garden
Industry/Entity Type
Home And Garden
Requirements
Nice to have
- Fall colors. Doesnt have to be exactly what was picked just needs to look like fall.

```html
<!DOCTYPE html>
<html lang="en">
<head>
<meta charset="UTF-8">
<title>Fresh for Fall! – Display Sign</title>
<link href="https://fonts.googleapis.com/css2?family=Lobster&family=Playball&family=Montserrat:wght@500&display=swap" rel="stylesheet">
<style>
  :root {
    --stage: #ebe8e3;
    --wood: #f7f7f7;
    --wood-line: rgba(150, 150, 150, 0.35);
    --title-top: #ffd23a;
    --title-bottom: #f27a1f;
    --red: #e33a4e;
    --orange: #f3823a;
    --green: #94c83d;
    --brand-green: #3d6b3a;
    --white: #ffffff;
  }
  * { box-sizing: border-box; margin: 0; padding: 0; }
  html, body {
    width: 762px; height: 1200px; overflow: hidden;
    background: var(--stage);
  }
  .sign {
    position: absolute; left: 115px; top: 20px;
    width: 531px; height: 1160px;
    background: var(--white);
    overflow: hidden;
    box-shadow: 0 4px 18px rgba(0,0,0,0.12);
  }
  .wood-panel {
    position: absolute; left: 0; top: 0; width: 531px; height: 886px;
    background:
      repeating-linear-gradient(135deg, transparent 0 66px, var(--wood-line) 66px 67.5px),
      var(--wood);
  }
  .photo { position: absolute; }
  .photo--tropical-leaves {
    right: 0; top: 0; width: 230px; height: 240px;
    background: radial-gradient(ellipse at 85% 10%, #7a1c3a 0%, #c2205f 40%, rgba(210,40,110,0) 72%);
  }
  .photo--mum {
    left: 0; top: 388px; width: 72px; height: 154px;
    background: radial-gradient(ellipse at 0% 50%, #ef6a1c 0%, #f48a2c 55%, rgba(244,138,44,0) 100%);
  }
  .photo--pumpkin {
    right: 0; top: 764px; width: 98px; height: 122px;
    background: radial-gradient(ellipse at 70% 80%, #e8661a 0%, #ef7d23 55%, rgba(239,125,35,0) 100%);
  }
  .title {
    position: absolute; left: 80px; top: 78px;
    font-family: "Lobster", cursive;
    font-weight: 400;
    line-height: 0.92;
    white-space: nowrap;
    background: linear-gradient(180deg, var(--title-top), var(--title-bottom));
    -webkit-background-clip: text; background-clip: text; color: transparent;
    filter: drop-shadow(0 0 2px #fff) drop-shadow(0 3px 4px rgba(0,0,0,0.18));
  }
  .title__line { display: block; font-size: 122px; }
  .title__line--second { padding-left: 10px; }
  .selling-point {
    position: absolute;
    display: flex; align-items: center; justify-content: center;
    text-align: center;
    font-family: "Playball", cursive;
    font-size: 50px; line-height: 1.05;
    border: 1.5px solid currentColor;
    white-space: nowrap;
  }
  .selling-point--decor { left: 90px; top: 344px; width: 343px; height: 151px; color: var(--red); transform: rotate(-0.4deg); }
  .selling-point--color { left: 93px; top: 514px; width: 332px; height: 143px; color: var(--orange); }
  .selling-point--air { left: 93px; top: 681px; width: 332px; height: 147px; color: var(--green); }
  .rainbow-band {
    position: absolute; left: 0; top: 886px; width: 531px; height: 8px;
    background: linear-gradient(90deg, #e02a52, #f7a21b 30%, #f6e21a 50%, #e58a3a 70%, #b43a8c);
  }
  .partner {
    position: absolute; top: 964px;
    display: flex; align-items: center; gap: 8px;
    font-family: "Montserrat", sans-serif; font-weight: 500;
    font-size: 24px; white-space: nowrap;
  }
  .partner--maker { left: 75px; color: var(--brand-green); }
  .partner--retailer { left: 338px; color: var(--brand-green); }
  .partner__mark { width: 26px; height: 26px; background: currentColor; flex: none; }
  .photo--leaf-border {
    left: 0; bottom: 0; width: 531px; height: 141px;
    background: linear-gradient(180deg, rgba(255,255,255,0) 0%, #f6c21c 35%, #ef8a1c 70%, #c8281f 100%);
  }
</style>
</head>
<body>
  <main class="sign">
    <div class="wood-panel"></div>
    <div class="photo photo--tropical-leaves" role="img" aria-label="Burgundy and pink tropical leaves"></div>
    <div class="photo photo--mum" role="img" aria-label="Orange chrysanthemum bloom"></div>
    <div class="photo photo--pumpkin" role="img" aria-label="Orange pumpkin with stem"></div>

    <h1 class="title">
      <span class="title__line">Fresh</span>
      <span class="title__line title__line--second">for Fall!</span>
    </h1>

    <p class="selling-point selling-point--decor">Natural Front<br>Door Decor</p>
    <p class="selling-point selling-point--color">Enjoy Warm &amp;<br>Cozy Color</p>
    <p class="selling-point selling-point--air">Generate Fall<br>Fresh Air</p>

    <div class="rainbow-band"></div>

    <div class="partner partner--maker"><span class="partner__mark"></span>Verdant Crafts</div>
    <div class="partner partner--retailer">Yard Vault</div>

    <div class="photo photo--leaf-border" role="img" aria-label="Row of red, orange and yellow autumn maple leaves"></div>
  </main>
</body>
</html>
```